Mobile Disc Jockey Service Brochure

We are looking for a brochure to showcase our Mobile DJ Business. It needs to be something professional looking and fit our target market of Weddings. We cater to events of all types but majority of our clients are brides looking for professional service at affordable prices.

Our website for reference: http://www.thesoundcaravan.com/
facebook for reference: https://www.facebook.com/MarcusSoundCaravan

I've uploaded a picture of us, our logo and some other photos that might be useful. Feel free to use additional stock photos that may be applicable to our project needs. Feel free to crop photos as necessary

I'd like this to be an 8 1/2" x 11" bifold, or trifold brochure, double sided. The front can be simple with our logo and phone number. Back can also be simple with a small logo and our website. I'd like one of the areas to focus on our bio and picture, and the other areas can describe our packages and what we offer as well as our mission statement

Some other information: We provide not only Professional and Enthusiastic DJ Services but we also do Uplighting as well as Event planning.

Target Market(s)

Weddings, Anniversary Parties, Birthdays, Themed Party

Industry/Entity Type

Business

Requirements
Must have
• Something describing our services like the following (feel free to rearrange the wording if necessary).
• All packages are hourly and custom built to fit your party needs. A list of our offerings includes:
• Cocktail music, dinner music, dance music
• Ultimate coordination of activities and unique event planning experience
• HD Sound
• LED Light Show
• Wireless Microphone System
• Unlimited choice of song titles from Digital to Vinyl
• Free travel within 50 miles - Travel outside of this is calculated with a fee per additional mile.
• Optional Services:
• Projector with Screen for Slide Shows & Movies
• Uplighting
• We provide a Fun & Easy to use web interface that walks you through the timeline of your event capturing every detail you desire, making planning fun! We guarantee you will hear everything you want, we have an endless music library as well as mobile internet so we can access any song you and your guests want instantly! In addition to the Online Event Planner, we offer unlimited consultations prior to your event to ensure face to face that you are getting everything you want and more.
• I'd like to see something featuring our services as well as our picture that I uploaded maybe cropped at the chest level or there abouts with this information:
• We are a husband and wife team. Marcus Halloway, the DJ has been providing custom soundtracks for events of all types for well over a decade. In 2011 his wife Tessa joined the team to handle all of the event coordination and logistics. Together we run the Sound Caravan offering Professional DJ Services at a personal level. We enjoy working with clients to create the event that they deserve at an affordable price. Contact us today for your quote or visit us online.
• (555) 314-2086
• thesoundcaravan@mailbox-example.com
• www.thesoundcaravan.com
• www.facebook.com/MarcusSoundCaravan
• Id also like something along the lines of:
• Your choice of DJ can make or break your event. The Sound Caravan guarantees to go above and beyond to make your event flawless and unforgettable. We promise to provide nothing but the best, well within your budget. When it comes to Weddings, we recognize that your Wedding is the most important day of your life! We will work with you side by side to ensure that it's everything you have dreamed of and more. Let the experience we provide create a beautiful memory that will last a lifetime.
• (Mission Statement)
• Our mission is to provide high quality and affordable mobile DJ services that will fill your event with beautiful lifelong memories.
Nice to have
• Id like to see the picture of the bride and grandfather dancing put in there somewhere.
• Color Scheme should be a mix of greys, black, white, you can add color as needed to match photos/logo, etc.

```html
<!DOCTYPE html>
<html lang="en">
<head>
<meta charset="utf-8">
<title>The Sound Caravan – Brochure Inside Spread</title>
<link href="https://fonts.googleapis.com/css2?family=Roboto:wght@300;400;700&family=Oswald:wght@500&display=swap" rel="stylesheet">
<style>
  :root{
    --orange:#f9b21b;
    --ink:#111111;
    --grey-text:#7a7a7a;
    --red:#d9261c;
    --white:#ffffff;
  }
  *{margin:0;padding:0;box-sizing:border-box}
  html,body{width:1200px;height:927px;overflow:hidden;background:var(--white)}
  body{font-family:"Roboto",Arial,sans-serif;font-weight:300;color:var(--grey-text)}
  .spread{position:relative;width:1200px;height:927px;overflow:hidden;background:var(--white)}

  .top-strip{position:absolute;left:0;top:14px;width:805px;height:28px;
    background:linear-gradient(90deg,#2a2a2a,#8a8a8a 20%,#e6e6e6 45%,#555 60%,#cfcfcf 80%,#eeeeee)}
  .top-accent{position:absolute;left:805px;top:0;width:395px;height:14px;background:var(--orange)}
  .top-accent-line{position:absolute;left:805px;top:42px;width:395px;height:10px;background:var(--orange)}

  .hero-photo{position:absolute;left:0;top:52px;width:1200px;height:250px;
    background:linear-gradient(90deg,#1b0f0c 0%,#3a201a 35%,#2c1611 60%,#4a2a20 80%,rgba(249,178,27,.6) 100%);
    -webkit-mask-image:linear-gradient(180deg,#000 75%,transparent);mask-image:linear-gradient(180deg,#000 75%,transparent)}
  .hero-headline{position:absolute;left:55px;top:140px;width:380px;color:var(--white);font-size:22px;line-height:30px;font-weight:300;z-index:2}

  .about-panel{position:absolute;left:805px;top:280px;width:395px;height:625px;background:var(--orange)}

  .offerings-title{position:absolute;left:55px;top:283px;width:360px;color:var(--orange);font-weight:700;font-size:17px;line-height:22px;z-index:2}
  .offerings{position:absolute;left:55px;top:361px;width:365px;list-style:none;font-size:14.5px;line-height:18px;color:var(--grey-text);z-index:3}
  .offerings li{position:relative;padding-left:26px;margin-bottom:10px}
  .offerings li::before{content:"";position:absolute;left:0;top:-1px;width:20px;height:20px;border-radius:50%;
    background:radial-gradient(circle at 35% 35%,#ff5a4a,var(--red))}

  .bride-photo{position:absolute;left:0;top:578px;width:275px;height:327px;z-index:1;
    background:linear-gradient(160deg,rgba(255,255,255,0) 0%,#8a1f3a 25%,#c0324f 50%,#3a0d1a 100%);
    -webkit-mask-image:linear-gradient(180deg,transparent,#000 20%);mask-image:linear-gradient(180deg,transparent,#000 20%)}

  .tagline{position:absolute;left:440px;top:310px;width:320px;text-align:center;font-size:25px;line-height:32px;color:var(--grey-text)}

  .bracket{position:absolute;left:775px;top:440px;width:28px;height:388px;border:2px solid #d9d9d9;border-left:none}
  .sound-photo{position:absolute;left:405px;top:462px;width:386px;height:346px;border:1px solid var(--orange);z-index:1;
    background:linear-gradient(90deg,rgba(255,255,255,.9) 0%,rgba(255,255,255,0) 14%),
      radial-gradient(ellipse at 60% 65%,#2a2a2a 0%,#3b3b3b 35%,#151515 60%,#6a6a6a 85%,#e8e8e8 100%)}
  .sound-caption{position:absolute;left:0;right:0;top:216px;text-align:center;color:var(--white);font-size:28px;line-height:36px;font-weight:400}
  .sound-caption .hd{color:var(--orange);font-weight:700}

  .arrow{position:absolute;left:376px;top:627px;z-index:2}
  .motto{position:absolute;left:300px;top:652px;width:100px;text-align:center;font-family:"Oswald",Arial,sans-serif;font-weight:500;font-size:13px;line-height:21px;color:var(--ink);letter-spacing:.5px;z-index:2}
  .motto .accent{color:var(--orange)}

  .bio-caption{position:absolute;left:300px;top:838px;width:480px;text-align:center;font-size:19px;line-height:25px;color:var(--grey-text)}

  .about-icon{position:absolute;left:852px;top:298px}
  .about-copy{position:absolute;left:852px;top:347px;width:308px;color:var(--white);font-size:12px;line-height:16px;text-align:justify}
  .about-copy h2{font-size:14px;font-weight:700;line-height:17px;text-align:left}
  .about-copy .lead{font-weight:700;font-size:13px}
  .about-copy p+p{margin-top:20px}
  .float-spacer{float:right;width:0;height:96px}
  .couple-photo{float:right;clear:right;width:146px;height:276px;margin-left:10px;border:2px solid var(--white);
    background:linear-gradient(180deg,#6c8a3c,#3d5a24 60%,#8c7a5a)}

  .brand-mark{position:absolute;left:918px;top:820px;width:170px;display:flex;align-items:center;gap:6px;font-weight:700;font-size:14px;color:var(--ink)}
  .brand-mark .dot{width:12px;height:12px;background:var(--ink);flex:none}

  .bottom-bar{position:absolute;left:0;top:905px;width:1200px;height:22px;background:linear-gradient(90deg,#222 0%,#222 85%,var(--orange))}
</style>
</head>
<body>
<main class="spread">
  <div class="top-strip" role="img" aria-label="Greyscale photo strip of DJ turntable equipment"></div>
  <div class="top-accent"></div>
  <div class="top-accent-line"></div>

  <div class="hero-photo" role="img" aria-label="Photo of a bride and groom dancing at a wedding reception"></div>
  <p class="hero-headline">We provide not only Professional,<br>Enthusiastic DJ Services but<br>we also do Uplighting as well as<br>Event planning.</p>

  <div class="about-panel"></div>

  <div class="bride-photo" role="img" aria-label="Photo of a bride twirling in her gown under pink uplighting"></div>

  <p class="tagline">We enjoy working with clients to create the event that they deserve at an affordable price.</p>

  <div class="bracket"></div>
  <div class="sound-photo" role="img" aria-label="Close-up photo of a black PA speaker">
    <p class="sound-caption">We provide<br><span class="hd">HD</span>Sound</p>
  </div>

  <h2 class="offerings-title">All packages are hourly and custom<br>built to fit your party needs. A list of<br>our offerings includes:</h2>
  <ul class="offerings">
    <li>Cocktail music, dinner music, dance music</li>
    <li>Ultimate coordination of activities<br>and unique event planning experience</li>
    <li>Wireless Microphone System</li>
    <li>Unlimited choice of song titles from Digital to Vinyl</li>
    <li>Free travel within 50 miles - Travel outside of this is<br>calculated with a fee per additional mile.</li>
    <li>HD Sound</li>
    <li>LED Light Show</li>
    <li>Uplighting</li>
    <li>Projector</li>
  </ul>

  <svg class="arrow" width="44" height="20" viewBox="0 0 44 20" aria-hidden="true">
    <polygon points="0,10 22,0 18,7 44,7 44,13 18,13 22,20" fill="#f9b21b"/>
  </svg>
  <p class="motto">Any Event<br><span class="accent">Any Playlist</span><br>Any Time</p>

  <p class="bio-caption">Marcus Halloway has been providing custom sound tracks for events of all types for well over a decade.</p>

  <svg class="about-icon" width="46" height="46" viewBox="0 0 46 46" aria-hidden="true">
    <rect width="46" height="46" rx="8" fill="#111"/>
    <circle cx="23" cy="23" r="15" fill="#f9b21b"/>
    <circle cx="23" cy="23" r="4" fill="#111"/>
    <line x1="33" y1="9" x2="26" y2="22" stroke="#fff" stroke-width="2.5" stroke-linecap="round"/>
  </svg>

  <section class="about-copy">
    <h2>About Us</h2>
    <div class="float-spacer"></div>
    <div class="couple-photo" role="img" aria-label="Photo of the husband and wife DJ team standing outdoors"></div>
    <p>We provide a Fun &amp; Easy to use web interface that walks you through the timeline of your event capturing every detail you desire, making planning fun! We guarantee you will hear everything you want, we have an endless music library as well as mobile internet so we can access any song you and your guests want instantly!</p>
    <p><span class="lead">We are a husband and wife team.</span> Marcus Halloway, the DJ has been providing custom sound tracks for events of all types for well over a decade. In 2011 his wife Tessa joined the team to handle all of the event coordination and logistics. Together we run the Sound Caravan offering Professional DJ Services at a personal level. We enjoy working with clients to create the event that they deserve at an affordable price. Contact us today for your quote or visit us online.</p>
  </section>

  <div class="brand-mark"><span class="dot"></span><span>the Sound Caravan</span></div>

  <div class="bottom-bar"></div>
</main>
</body>
</html>
```